new roofing company card

New primary business card for roofing company.

Industry/Entity Type

Residential roofing/Specializing in Asphalt and Standing seam metal roofing

Contact Information for Business Card

Phone number is: 484 672 1058 Email: support@fennridgeroofworks.com website: www.fennridgeroofworks.com

Colors
EB3D1F
EC4F4E
F09395
F8D3D4
FCEDEE

```html
<!DOCTYPE html>
<html lang="en">
<head>
<meta charset="utf-8">
<title>Fennridge Roofworks – Business Card</title>
<link rel="stylesheet" href="https://fonts.googleapis.com/css2?family=Montserrat:wght@500;700&display=swap">
<style>
  :root {
    --bg: #e3e3e3;
    --card: #ffffff;
    --red: #b81e26;
    --ink: #262626;
    --text: #1e1e1e;
  }
  * { box-sizing: border-box; margin: 0; padding: 0; }
  html, body { width: 1200px; height: 900px; overflow: hidden; }
  body {
    background: var(--bg);
    font-family: "Montserrat", sans-serif;
    position: relative;
  }
  .card {
    position: absolute;
    width: 560px;
    height: 320px;
    background: var(--card);
    box-shadow: 0 10px 24px rgba(0,0,0,0.18);
    overflow: hidden;
  }
  .card--front { left: 70px; top: 110px; }
  .card--back { left: 570px; top: 470px; }

  .wordmark {
    display: flex;
    align-items: center;
    gap: 12px;
    color: var(--ink);
    font-weight: 700;
    line-height: 1.05;
    text-transform: uppercase;
    letter-spacing: 0.04em;
  }
  .wordmark__square {
    width: 22px;
    height: 22px;
    background: var(--red);
    flex: none;
  }
  .card--front .wordmark {
    position: absolute;
    left: 0; right: 0; top: 0; bottom: 0;
    justify-content: center;
    font-size: 34px;
  }
  .card--front .wordmark__square { width: 30px; height: 30px; }

  .card--back .wordmark {
    position: absolute;
    left: 46px;
    top: 108px;
    font-size: 21px;
  }
  .divider {
    position: absolute;
    left: 280px;
    top: 74px;
    width: 2px;
    height: 118px;
    background: var(--red);
  }
  .contact {
    position: absolute;
    left: 300px;
    top: 84px;
    list-style: none;
    font-size: 11.5px;
    font-weight: 500;
    color: var(--text);
  }
  .contact li {
    display: flex;
    align-items: center;
    gap: 7px;
    margin-bottom: 6px;
  }
  .contact svg { width: 11px; height: 11px; flex: none; fill: var(--red); }
  .wave { position: absolute; left: 0; top: 0; width: 560px; height: 320px; }
</style>
</head>
<body>
  <section class="card card--front" aria-label="Card front">
    <div class="wordmark">
      <span class="wordmark__square"></span>
      <span>Fennridge<br>Roofworks</span>
    </div>
  </section>

  <section class="card card--back" aria-label="Card back">
    <svg class="wave" viewBox="0 0 560 320" aria-hidden="true">
      <path d="M0 292 C150 268 260 250 360 215 C450 184 520 150 560 120 L560 320 L0 320 Z" fill="var(--red)"/>
      <path d="M40 286 C150 252 250 238 350 205 C440 175 505 142 540 112 C510 146 445 184 352 212 C255 242 150 260 40 286 Z" fill="var(--ink)"/>
    </svg>

    <div class="wordmark">
      <span class="wordmark__square"></span>
      <span>Fennridge<br>Roofworks</span>
    </div>

    <div class="divider"></div>

    <ul class="contact">
      <li>
        <svg viewBox="0 0 24 24"><path d="M6.6 10.8a15.1 15.1 0 0 0 6.6 6.6l2.2-2.2c.3-.3.7-.4 1-.2 1.1.4 2.3.6 3.6.6.6 0 1 .4 1 1V20c0 .6-.4 1-1 1C10.6 21 3 13.4 3 4c0-.6.4-1 1-1h3.5c.6 0 1 .4 1 1 0 1.3.2 2.5.6 3.6.1.3 0 .7-.2 1z"/></svg>
        484 672 1058
      </li>
      <li>
        <svg viewBox="0 0 24 24"><path d="M2 5h20v14H2z M2 5l10 8 10-8" /></svg>
        support@fennridgeroofworks.com
      </li>
      <li>
        <svg viewBox="0 0 24 24"><circle cx="12" cy="12" r="10"/></svg>
        www.fennridgeroofworks.com
      </li>
    </ul>
  </section>
</body>
</html>
```